BUSINESS CARD - HALVERDINE RURAL SERVICES

I would like to create a business card for my fertilizer spreading business. I would like to incorporate my existing logo and also a description of the services offered. The business card will be given to farmers so must be kept simple but effective. It will also be left in stores so much also be eye catching in order to stand out from other cards.

Target Market(s)

FARMERS

Requirements
Must have
• FRONT OF CARD = EXISTING LOGO + "CUSTOMISED SPREADING" below the logo

REAR Of CARD = SERVICES OFFERED AND CONTACT DETAILS

- Bulk fertilizer including Lime, Gypsum, Manure & Compost
- Granular fertilizer including Single Super, Urea, Gran-am, & Custom Blends
- Modern equipment - Autosteer & Variable Rate Capable
- Friendly & Reliable Service
- Contact Gus: 0471 502 318
Nice to have
• utilize same color scheme as existing logo

```html
<!DOCTYPE html>
<html lang="en">
<head>
<meta charset="utf-8">
<title>Halverdine Rural Services – Business Card</title>
<link rel="stylesheet" href="https://fonts.googleapis.com/css2?family=Montserrat:wght@600;700;800&family=Open+Sans:wght@400;600&display=swap">
<style>
  :root {
    --orange: #e8912a;
    --charcoal: #454545;
    --card-white: #f7f7f5;
    --backdrop: #dcdcdc;
    --phone-white: #ffffff;
  }
  * { box-sizing: border-box; margin: 0; padding: 0; }
  html, body { width: 1200px; height: 1200px; overflow: hidden; }
  body {
    background: var(--backdrop);
    display: flex;
    flex-direction: column;
    align-items: center;
    justify-content: center;
    gap: 60px;
    font-family: "Open Sans", Arial, sans-serif;
  }
  .card {
    position: relative;
    width: 840px;
    height: 480px;
    overflow: hidden;
    box-shadow: 0 14px 30px rgba(0,0,0,0.18);
  }

  /* Front */
  .card-front {
    background: var(--card-white);
    display: flex;
    flex-direction: column;
    align-items: center;
    justify-content: center;
    gap: 26px;
  }
  .brand {
    display: flex;
    align-items: center;
    gap: 18px;
  }
  .brand-dot {
    width: 62px; height: 62px;
    border-radius: 50%;
    background: var(--charcoal);
    flex: none;
  }
  .brand-name {
    font-family: "Montserrat", Arial, sans-serif;
    font-weight: 700;
    color: var(--charcoal);
    font-size: 36px;
    line-height: 1.1;
  }
  .tagline {
    font-family: "Montserrat", Arial, sans-serif;
    font-weight: 600;
    color: var(--charcoal);
    font-size: 24px;
    letter-spacing: 0.42em;
    text-transform: uppercase;
  }

  /* Back */
  .card-back { background: var(--orange); }
  .logo-disc {
    position: absolute;
    left: -90px; top: -40px;
    width: 460px; height: 460px;
    border-radius: 50%;
    background: var(--card-white);
    display: flex;
    align-items: center;
    justify-content: flex-end;
    padding-right: 40px;
  }
  .logo-disc .brand { flex-direction: column; gap: 12px; }
  .logo-disc .brand-dot { width: 70px; height: 70px; }
  .logo-disc .brand-name { font-size: 25px; text-align: center; }
  .services-disc {
    position: absolute;
    left: 420px; top: -120px;
    width: 720px; height: 720px;
    border-radius: 50%;
    background: var(--card-white);
  }
  .services {
    position: absolute;
    left: 465px; top: 140px;
    width: 360px;
  }
  .services-title {
    font-family: "Montserrat", Arial, sans-serif;
    font-weight: 800;
    font-size: 24px;
    letter-spacing: 0.04em;
    color: #222;
    text-transform: uppercase;
    margin-bottom: 12px;
  }
  .services-list {
    list-style: none;
    color: var(--orange);
    font-weight: 600;
    font-size: 16.5px;
    line-height: 1.45;
  }
  .contact {
    position: absolute;
    left: 40px; bottom: 34px;
    display: flex;
    align-items: center;
    gap: 12px;
    color: var(--phone-white);
    font-family: "Montserrat", Arial, sans-serif;
    font-weight: 700;
    font-size: 24px;
    letter-spacing: 0.04em;
  }
  .contact svg { width: 22px; height: 22px; }
</style>
</head>
<body>
  <section class="card card-front" aria-label="Card front">
    <div class="brand">
      <span class="brand-dot" aria-hidden="true"></span>
      <span class="brand-name">Halverdine Rural<br>Services</span>
    </div>
    <p class="tagline">Customised Spreading</p>
  </section>

  <section class="card card-back" aria-label="Card back">
    <div class="logo-disc">
      <div class="brand">
        <span class="brand-dot" aria-hidden="true"></span>
        <span class="brand-name">Halverdine Rural<br>Services</span>
      </div>
    </div>
    <div class="services-disc" aria-hidden="true"></div>
    <div class="services">
      <h2 class="services-title">Services Offered</h2>
      <ul class="services-list">
        <li>Bulk fertilizer including Lime, Gypsum, Manure &amp; Composts</li>
        <li>- Granular fertilizer including Single Super, Urea, Gran-am, &amp; Custom Blends</li>
        <li>- Modern equipment</li>
        <li>- Friendly &amp; Reliable Services</li>
      </ul>
    </div>
    <div class="contact">
      <svg viewBox="0 0 24 24" aria-hidden="true"><path fill="currentColor" d="M6.6 10.8a15.1 15.1 0 0 0 6.6 6.6l2.2-2.2a1 1 0 0 1 1-.25 11.4 11.4 0 0 0 3.6.57 1 1 0 0 1 1 1V20a1 1 0 0 1-1 1A17 17 0 0 1 3 4a1 1 0 0 1 1-1h3.5a1 1 0 0 1 1 1c0 1.25.2 2.45.57 3.57a1 1 0 0 1-.25 1z"/></svg>
      <span>0471 502 318</span>
    </div>
  </section>
</body>
</html>
```